Design Creative Banner or Gif Ads. 3 Designs To Be Selected

Come up with some creative banner ads for crestline.co.nz

*At least 3 different winning banners will be chosen*

Please provide banner ads / gif ads in common google ads / website banner formats.

They can be gif or static but must stand out while still maintaining clear clean text and visuals, with a premium professional feel (please avoid clip art or anything that gives a cheap message).

Please keep in mind that these will likely be small ads so text needs to be large and if there's there a lot of text then use multiple frames/ pages as submit as a gif.

Style
Minimal & clean lines
Architectural or realistic images
Avoid cartoon styles, clipart, or anything that looks cheap

Font
Nexa or Montserrat or similar

Tone
Premium, serious, trustworthy — fits new builds

Colours
Option 1: Deep Navy (trust & quality) & lighter blues and warm grey
Option 2: Open to bright colours to help the ads stand out, such as (but not limited to) bright pink with black, yellow, fluorescent green, provided the messaging is still done professionally.
Our logo is attached (Crest Line Logo)

Display Sizes
Ad specs for file sizes should be file formats like JPEG, GIF, and PNG, with animations limited to a max of 30 seconds or less.
We will need several different ad sizes provided for each of the 3 selected winning designs.

• Medium Rectangle: 300 × 250 pixels
• Leaderboard: 728 × 90 pixels
• Desktop Banner ad image: (640x360 pixels)
• Desktop Banner ad image 2: (300x600 pixels)
• Possibly one or two other sizes

Flexibility to be creative
The ad text, words, upper/lower case, layout, colour, theme, and images can be adjusted to how you think it will look best. The follow example ads are just examples of what we are after but we are keen to see what you can create.

Recommendations at this point:
1. Avoid text heavy
2. Looking for more Gif ads
3. Imaging: if possible use real stock photo's rather than AI

Themes:

1
Building Soon? Start Here
Free Build Planning Pack:
✓ Build Cost Calculator
✓ Hidden Cost Checklist
✓ Builder Comparison Guide
Build With Confidence
Download Free

2
Before You Choose A Builder
Compare Price, Scope, Risk & Value
Avoid Costly Mistakes
Choose The Right Builder With Confidence
Download The Free Guide

3
Planning A New Build?
Avoid These Common Mistakes:
✗ Hidden Exclusions
✗ Missing Scope
✗ Unrealistic Allowances
✗ Budget Blowouts
Download The Free Guide

4
Before You Buy Land
Know what it could cost to build.
Avoid Costly Building Mistakes
Download Our Free Guides

5
Know Your Build Budget?
• Free Build Cost Calculator
• Hidden Cost Checklist
• Build Planning Tools
Calculate Costs (Download)

Target Market(s)

Landowners looking to build

Industry/Entity Type

Building

Font styles to use
Other font styles liked:
• Nexa or Montserrat or similar

Requirements
Should not have
• Avoid cartoon styles, clipart, or anything that looks cheap

```html
<!DOCTYPE html>
<html lang="en">
<head>
<meta charset="utf-8">
<title>Crest Line – Banner Ad Set</title>
<link rel="stylesheet" href="https://fonts.googleapis.com/css2?family=Inter:ital,wght@0,400;0,600;0,700;0,800;1,400&family=Montserrat:wght@400;600;700&display=swap">
<style>
  :root{
    --board:#c5dfe3;
    --navy:#18294a;
    --navy-deep:#14244f;
    --ink:#0d1424;
    --white:#ffffff;
    --paper:#f3f3ef;
    --cream:#f3e6b8;
    --gold:#f2c45c;
    --orange:#f3a94a;
    --salmon:#f5a071;
    --sand:#f6d38e;
    --tan:#d8a86a;
    --sky:#2f9ae6;
    --ice:#c9f0f6;
    --teal:#1aa0c0;
    --blue:#1f6fb8;
    --royal:#1a3d8c;
    --book-top:#4d76a6;
    --book-bot:#3e6fa8;
  }
  *{box-sizing:border-box;margin:0;padding:0}
  html,body{width:997px;height:1200px;overflow:hidden;background:var(--board)}
  body{position:relative;font-family:"Inter",Arial,sans-serif;color:var(--white)}

  .banner{position:absolute;width:395px;height:329px;overflow:hidden;box-shadow:0 10px 18px rgba(20,40,60,.28)}
  .photo{position:absolute;inset:0}
  .abs{position:absolute}
  .wave{position:absolute;top:0}

  .brand{position:absolute;display:flex;align-items:flex-start;gap:7px}
  .brand-mark{width:26px;height:22px;background:var(--navy);margin-top:1px}
  .brand-name{font-family:"Montserrat",sans-serif;font-weight:600;font-size:14px;color:var(--navy);line-height:1}
  .brand-tag{font-family:"Montserrat",sans-serif;font-weight:600;font-size:3.6px;letter-spacing:.1px;color:#5b7ea6;margin-top:3px;white-space:nowrap}

  .headline{font-weight:800;line-height:1;letter-spacing:-.3px}

  .btn{position:absolute;display:flex;align-items:center;justify-content:center;text-align:center;font-weight:700;line-height:1.05;letter-spacing:.3px}

  .guide-book{position:absolute;background:linear-gradient(160deg,var(--book-top),var(--book-bot));box-shadow:2px 3px 8px rgba(0,0,0,.35);font-family:"Montserrat",sans-serif}
  .guide-book .book-title{color:var(--navy-deep);font-weight:700;line-height:1.08}
  .guide-book .book-sub{color:#e9f1fa;font-weight:400;line-height:1.1}
  .guide-book .book-note{color:#cfe0f2;line-height:1.3}
  .guide-book .book-url{color:#cfe0f2}

  /* Building soon */
  .ad-start{left:79px;top:57px}
  .ad-start .photo{background:linear-gradient(180deg,#6b6a64 0%,#8a7e6c 35%,#5e6470 58%,#2f3b55 75%,#1f2b45 100%)}
  .ad-start .line-1{left:22px;top:218px;font-size:35px;color:var(--cream)}
  .ad-start .line-2{left:22px;top:251px;font-size:35px;color:var(--gold)}
  .ad-start .start-here{left:151px;top:263px;font-size:13px;font-weight:800;color:var(--orange)}
  .ad-start .tagline{right:23px;top:244px;font-size:12.5px;font-weight:800;color:var(--gold);text-align:right;line-height:.95}
  .ad-start .btn{left:293px;top:270px;width:80px;height:17px;background:var(--salmon);font-size:6.5px}
  .ad-start .pack-title{left:26px;top:289px;font-size:10.5px;font-weight:400}
  .ad-start .pack-list{left:21px;top:305px;font-size:9.2px;color:#ebc97b;white-space:nowrap;word-spacing:1px}

  /* Choose a builder */
  .ad-builder{left:78px;top:433px;height:329px}
  .ad-builder .photo{background:linear-gradient(180deg,#a7a9ae 0%,#9b9ea5 40%,#6c7487 65%,#2f3b57 88%,#24304b 100%)}
  .ad-builder .headline{left:19px;top:18px;font-size:35px;line-height:31px}
  .ad-builder .closer{right:24px;top:247px;font-size:12.5px;font-weight:700;text-align:right;line-height:13px}
  .ad-builder .compare{left:22px;top:292px;font-size:16.5px;font-weight:800;color:var(--orange)}
  .ad-builder .compare-note{left:114px;top:295px;font-size:10px;font-style:italic;font-weight:400}
  .ad-builder .btn{left:290px;top:294px;width:80px;height:17px;background:var(--sand);color:var(--navy);font-size:6.8px}

  /* Planning a new build */
  .ad-planning{left:81px;top:807px;height:328px}
  .ad-planning .photo{background:linear-gradient(180deg,#6f7f96 0%,#5a5e63 35%,#4a4c4f 60%,#2a3346 85%,#1f2840 100%)}
  .ad-planning .headline{left:165px;top:166px;font-size:27.5px;font-weight:700;color:var(--orange);line-height:27px}
  .ad-planning .subhead{left:164px;top:230px;font-size:9.8px;font-weight:700;color:#f3d35f}
  .ad-planning .mistakes{left:164px;top:245px;font-size:10px;line-height:10.4px;list-style:none}
  .ad-planning .btn{left:281px;top:288px;width:96px;height:21px;background:#15223d;border:1px solid #33425f;color:#7fb5e8;font-size:6.5px}

  /* Before you buy land */
  .ad-land{left:521px;top:250px}
  .ad-land .photo{background:linear-gradient(180deg,#9cb4c4 0%,#5e7a3c 22%,#4f6c34 40%,#88a39a 52%,#3f7f96 70%,#1f5f8f 100%)}
  .ad-land .headline{left:20px;top:189px;font-size:39.5px;line-height:37px}
  .ad-land .headline .accent{color:var(--ice)}
  .ad-land .cost-note{left:137px;top:269px;font-size:9.8px;font-weight:700;color:#b8dcee;line-height:9.5px}
  .ad-land .btn{left:248px;top:272px;width:112px;height:25px;background:var(--sky);font-size:9.5px}

  /* Know your build budget */
  .ad-budget{left:521px;top:629px;width:396px;height:327px}
  .ad-budget .photo{background:linear-gradient(180deg,#e9ebea 0%,#d6d4cc 45%,#9aa3b8 62%,#243e7c 78%,#162c66 100%)}
  .ad-budget .headline{left:26px;top:81px;font-size:43px;line-height:39px;letter-spacing:-.5px}
  .ad-budget .w-know{color:var(--teal)}
  .ad-budget .w-your{color:var(--blue)}
  .ad-budget .w-build{color:var(--royal)}
  .ad-budget .w-budget{color:var(--ink)}
  .ad-budget .tools{left:26px;top:250px;font-size:13.5px;line-height:13.8px;list-style:none}
  .ad-budget .tools li::before{content:"• ";font-size:11px}
  .ad-budget .calc{left:257px;top:260px;width:112px;text-align:center;font-size:11.5px;font-weight:700;color:#e9a65a}
  .ad-budget .btn{left:275px;top:281px;width:80px;height:17px;background:var(--tan);color:var(--navy);font-size:8px}
</style>
</head>
<body>

<!-- Building soon -->
<section class="banner ad-start">
  <div class="photo" role="img" aria-label="Person using a smartphone calculator beside a small model house on a desk with plans"></div>
  <svg class="wave" width="200" height="92" viewBox="0 0 200 92" aria-hidden="true"><path d="M0 0H196C180 40 140 55 80 60C40 64 15 76 0 90Z" fill="var(--paper)"/></svg>
  <div class="brand" style="left:11px;top:11px">
    <div class="brand-mark"></div>
    <div><div class="brand-name">Crest Line</div><div class="brand-tag">COMPARE QUOTES FROM TRUSTED BUILDERS</div></div>
  </div>
  <div class="abs headline line-1">BUILDING</div>
  <div class="abs headline line-2">SOON?</div>
  <div class="abs start-here">START HERE</div>
  <svg class="abs" style="left:151px;top:257px" width="82" height="30" aria-hidden="true"><line x1="0" y1="0.5" x2="82" y2="0.5" stroke="#f3a94a" stroke-width=".6"/><line x1="0" y1="20" x2="66" y2="20" stroke="#f3a94a" stroke-width=".6"/></svg>
  <div class="abs tagline">Build With<br>Confidence</div>
  <div class="btn">DOWNLOAD FREE</div>
  <div class="abs pack-title">FREE BUILD PLANNING PACK:</div>
  <div class="abs pack-list">✓ Build Cost Calculator &nbsp;✓ Hidden Cost Checklist &nbsp;✓ Builder Comparison Guide</div>
</section>

<!-- Choose a builder -->
<section class="banner ad-builder">
  <div class="photo" role="img" aria-label="Professional woman in a dark blazer holding a notebook and pen, thinking"></div>
  <div class="brand" style="left:266px;top:12px">
    <div class="brand-mark"></div>
    <div><div class="brand-name">Crest Line</div><div class="brand-tag">COMPARE QUOTES FROM TRUSTED BUILDERS</div></div>
  </div>
  <div class="abs headline">BEFORE<br>YOU<br>CHOOSE A<br>BUILDER</div>
  <div class="guide-book" style="left:21px;top:150px;width:105px;height:130px;padding:12px 12px">
    <div class="book-title" style="font-size:10px">Avoid Costly<br>Build Mistakes</div>
    <div class="book-sub" style="font-size:10px;margin-top:10px">Free Build<br>Planning<br>Guides</div>
    <div class="book-note" style="font-size:4.6px;margin-top:8px">Compare Builders On Price,<br>Scope, Risk &amp; Value</div>
    <div class="book-url" style="font-size:4.4px;margin-top:8px">crestline.co.nz</div>
  </div>
  <div class="abs closer">Choose The<br>Right Builder<br>With Confidence</div>
  <div class="abs compare">COMPARE</div>
  <div class="abs compare-note">Price, Scope, Risk &amp; Value</div>
  <svg class="abs" style="left:108px;top:285px" width="130" height="36" aria-hidden="true"><ellipse cx="65" cy="18" rx="63" ry="16" fill="none" stroke="#e9a65a" stroke-width=".8"/></svg>
  <div class="btn">DOWNLOAD FREE</div>
</section>

<!-- Planning a new build -->
<section class="banner ad-planning">
  <div class="photo" role="img" aria-label="Multi-storey concrete building under construction with scaffolding"></div>
  <svg class="wave" width="395" height="110" viewBox="0 0 395 110" aria-hidden="true"><path d="M0 0H162C140 30 110 40 70 44C35 48 12 60 0 80Z" fill="var(--paper)"/></svg>
  <div class="brand" style="left:9px;top:9px">
    <div class="brand-mark"></div>
    <div><div class="brand-name">Crest Line</div><div class="brand-tag">COMPARE QUOTES FROM TRUSTED BUILDERS</div></div>
  </div>
  <div class="guide-book" style="left:20px;top:134px;width:134px;height:168px;padding:14px 16px">
    <div class="book-title" style="font-size:13px">Avoid Costly<br>Build Mistakes</div>
    <div class="book-sub" style="font-size:13px;margin-top:12px">Free Build<br>Planning<br>Guides</div>
    <div class="book-note" style="font-size:6px;margin-top:10px">Compare Builders On Price,<br>Scope, Risk &amp; Value</div>
    <div class="book-url" style="font-size:5.4px;margin-top:12px">crestline.co.nz</div>
  </div>
  <div class="abs headline">Planning A<br>New Build?</div>
  <div class="abs subhead">Avoid These Common Mistakes:</div>
  <ul class="abs mistakes">
    <li>✗ Hidden Exclusions</li>
    <li>✗ Missing Scope</li>
    <li>✗ Unrealistic Allowances</li>
    <li>✗ Budget Blowouts</li>
  </ul>
  <div class="btn">DOWNLOAD THE<br>FREE GUIDE</div>
</section>

<!-- Before you buy land -->
<section class="banner ad-land">
  <div class="photo" role="img" aria-label="Tropical coastline with palm trees above a sandy beach and clear water"></div>
  <svg class="wave" style="right:0" width="160" height="72" viewBox="0 0 160 72" aria-hidden="true"><path d="M0 0H160V70C120 66 90 64 64 54C34 42 12 22 0 0Z" fill="var(--paper)"/></svg>
  <div class="brand" style="left:265px;top:12px">
    <div class="brand-mark"></div>
    <div><div class="brand-name">Crest Line</div><div class="brand-tag">COMPARE QUOTES FROM TRUSTED BUILDERS</div></div>
  </div>
  <div class="guide-book" style="left:237px;top:90px;width:133px;height:166px;padding:14px 15px">
    <div class="book-title" style="font-size:13px">Avoid Costly<br>Build Mistakes</div>
    <div class="book-sub" style="font-size:13px;margin-top:13px">Free Build<br>Planning<br>Guides</div>
    <div class="book-note" style="font-size:6px;margin-top:11px">Compare Builders On Price,<br>Scope, Risk &amp; Value</div>
    <div class="book-url" style="font-size:5.4px;margin-top:12px">crestline.co.nz</div>
  </div>
  <div class="abs headline">BEFORE<br>YOU BUY<br><span class="accent">LAND</span></div>
  <div class="abs cost-note">KNOW WHAT IT<br>COULD COST TO<br>BUILD</div>
  <div class="btn">Download Our<br>Free Guides</div>
</section>

<!-- Know your build budget -->
<section class="banner ad-budget">
  <div class="photo" role="img" aria-label="Hands counting banknotes and holding a pen over a desk"></div>
  <div class="brand" style="left:11px;top:8px">
    <div class="brand-mark"></div>
    <div><div class="brand-name">Crest Line</div><div class="brand-tag">COMPARE QUOTES FROM TRUSTED BUILDERS</div></div>
  </div>
  <div class="abs headline"><span class="w-know">KNOW</span><br><span class="w-your">YOUR</span><br><span class="w-build">BUILD</span><br><span class="w-budget">BUDGET?</span></div>
  <ul class="abs tools">
    <li>Free Build Cost Calculator</li>
    <li>Hidden Cost Checklist</li>
    <li>Build Planning Tools</li>
  </ul>
  <div class="abs calc">CALCULATE COSTS</div>
  <div class="btn">DOWNLOAD</div>
</section>

</body>
</html>
```